Wordpress Theme, Folder, Brochure

Hello,

I have 3 projects that need to be completed and they all need to be the same theme.

Wordpress Theme:
Design homepage and one internal page

Print Folder:
I need a folder designed to match the website

Trifold Brochure:
I need a generic tri-fold brochure build to match the theme

Please find the attached file for more info.

Dale

```html
<!DOCTYPE html>
<html lang="en">
<head>
<meta charset="utf-8">
<title>Keystone PEO</title>
<link href="https://fonts.googleapis.com/css2?family=Questrial&display=swap" rel="stylesheet">
<style>
:root{
  --blue:#0b79c3;
  --blue-dark:#0a6aad;
  --ink:#222;
  --muted:#555;
  --light-bg:#f0f0f0;
  --footer:#2b2b2b;
  --footer-text:#b9b9b9;
  --white:#fff;
  --login:#1b1b1b;
}
*{margin:0;padding:0;box-sizing:border-box}
html,body{width:909px;height:1200px;overflow:hidden}
body{font-family:"Questrial",sans-serif;color:var(--ink);background:var(--white);position:relative}
.abs{position:absolute}
a{color:inherit;text-decoration:none}

/* header */
.brand{left:98px;top:30px;font-size:26px;color:var(--blue);letter-spacing:-.5px;display:flex;align-items:center;gap:6px}
.brand-dot{width:12px;height:12px;border-radius:50%;background:var(--blue)}
.top-links{right:295px;top:14px;font-size:10px;color:var(--ink)}
.top-links span{margin:0 3px}
.search{left:624px;top:8px;width:186px;height:20px;background:#f1f1f1;font-size:6px;color:#ccc;padding:5px 6px}
.search svg{position:absolute;right:5px;top:4px}
.phone{right:99px;top:35px;font-size:22px;display:flex;align-items:center;gap:4px}

/* nav */
.nav{left:0;top:72px;width:909px;height:40px;background:var(--blue)}
.nav ul{list-style:none;position:absolute;left:101px;top:13px;display:flex;font-size:11.5px;color:var(--white)}
.nav li{margin-right:18px}
.login{left:737px;top:79px;width:73px;height:24px;background:var(--login);color:var(--white);font-size:10px;font-weight:bold;display:flex;align-items:center;padding-left:9px;gap:6px}

/* hero */
.hero{left:0;top:112px;width:909px;height:397px;background:linear-gradient(90deg,#d8d6d2 0%,#8f7d70 35%,#6d5a4c 55%,#c9b5a2 75%,#dcd0c4 100%)}
.hero-card{left:98px;top:251px;width:424px;height:110px;background:rgba(40,40,40,.88);color:var(--white);padding:20px 13px}
.hero-card h1{font-weight:normal;font-size:24px;margin-bottom:8px}
.hero-card p{font-size:11.2px;line-height:23px}
.hero-btn{left:98px;top:366px;width:212px;height:39px;background:var(--blue);color:var(--white);font-size:15px;letter-spacing:.5px;display:flex;align-items:center;padding-left:20px}
.hero-btn svg{position:absolute;right:10px;top:5px}
.dots{left:98px;top:430px;display:flex;gap:4px}
.dots i{width:12px;height:12px;border-radius:50%;background:var(--white)}
.dots i.on{background:var(--blue)}

/* welcome */
.welcome{left:0;top:509px;width:909px;height:444px;background:var(--light-bg)}
.welcome h2{position:absolute;top:20px;width:100%;text-align:center;font-weight:normal;font-size:20px;color:var(--blue)}
.welcome p{position:absolute;left:98px;top:54px;width:712px;text-align:center;font-size:11.3px;line-height:18.2px;color:var(--muted)}
.col-title{top:682px;font-size:15px;color:var(--ink);font-weight:normal}
.service-box{top:707px;width:228px;height:220px;background:var(--blue);color:var(--white);padding:11px 0 0 21px}
.service-box ul{list-style:none;font-size:11.6px;line-height:19.5px}
.slide-arrow{top:787px}

/* footer */
.footer{left:0;top:953px;width:909px;height:247px;background:var(--footer)}
.f-head{top:982px;font-size:11px;font-weight:bold;color:var(--white);letter-spacing:.3px}
.f-list{list-style:none;font-size:9.5px;color:var(--footer-text)}
.news-text{left:463px;top:1011px;width:158px;font-size:9.5px;line-height:15px;color:var(--footer-text);text-align:justify}
.field{left:463px;width:168px;height:20px;background:var(--white);border:1px solid #ccc;font-size:9px;color:#aaa;padding:4px 10px}
.subscribe{left:557px;top:1108px;width:74px;height:18px;border-radius:9px;background:var(--blue);color:var(--white);font-size:10px;text-align:center;line-height:18px}
.social{left:705px;width:106px;height:20px;display:flex;justify-content:space-between;align-items:center;font-size:9.5px;color:var(--footer-text)}
.social i{width:21px;height:21px;border-radius:50%;background:var(--white)}
.copy{left:0;top:1168px;width:909px;text-align:center;font-size:9.5px;color:var(--footer-text)}
</style>
</head>
<body>

<header>
  <div class="abs brand"><span>Keystone PEO</span><span class="brand-dot"></span></div>
  <nav class="abs top-links"><a>Home</a><span>|</span><a>About Us</a><span>|</span><a>Request a Quote</a><span>|</span><a>Contact Us</a><span>|</span><a>Sitemap</a><span>|</span><a>Demo</a></nav>
  <div class="abs search">Type search
    <svg width="10" height="10" viewBox="0 0 10 10"><circle cx="4" cy="4" r="3" fill="none" stroke="#999" stroke-width="1.2"/><line x1="6.2" y1="6.2" x2="9.2" y2="9.2" stroke="#999" stroke-width="1.4"/></svg>
  </div>
  <div class="abs phone">
    <svg width="16" height="20" viewBox="0 0 16 20"><path d="M4 1 L7 5 L5 7 Q6 11 9 14 L11 12 L15 15 L12 19 Q4 17 1 6 Z" fill="#333"/></svg>
    <span>1-888-555-0147</span>
  </div>
</header>

<div class="abs nav">
  <ul><li>Payroll Services</li><li>HR Solutions</li><li>Online Solutions</li><li style="margin-right:22px">Workers Comp</li><li style="margin-right:22px">Employee's Benefit's</li><li>Resources</li></ul>
</div>
<div class="abs login">LOGIN <span style="font-weight:normal">|</span>
  <svg width="8" height="6" viewBox="0 0 8 6"><path d="M1 1 L4 4 L7 1" fill="none" stroke="#fff" stroke-width="1.6"/></svg>
</div>

<section class="abs hero" role="img" aria-label="Photo of a smiling businesswoman in an office with colleagues seated at a meeting table behind her"></section>
<div class="abs hero-card">
  <h1>Advantage Keystone PEO</h1>
  <p>By turning your back office over to Keystone PEO, you gain a business partner with the expertise you need to ensure your business stays in compliance.</p>
</div>
<a class="abs hero-btn">REQUEST A QUOTE
  <svg width="28" height="28" viewBox="0 0 28 28"><circle cx="14" cy="14" r="13" fill="#1a2a3a"/><path d="M11 7 L18 14 L11 21" fill="none" stroke="#fff" stroke-width="2.4"/></svg>
</a>
<div class="abs dots"><i class="on"></i><i></i><i></i><i></i></div>

<section class="abs welcome">
  <h2>Welcome To Keystone Peo</h2>
  <p>Lorem Ipsum is simply dummy text of the printing and typesetting industry. Lorem Ipsum has been the industry's standard dummy text ever since the 1500s, when an unknown printer took a galley of type and scrambled it to make a type specimen book. Lorem Ipsum is simply dummy text of the printing and typesetting industry. Lorem Ipsum has been the industry's standard dummy text ever since the 1500s, when an unknown printer took a galley of type and scrambled it to make a type specimen book.</p>
</section>

<h3 class="abs col-title" style="left:98px">Human Resources</h3>
<h3 class="abs col-title" style="left:341px">Payroll Services</h3>
<h3 class="abs col-title" style="left:582px">Worker's Camp</h3>

<div class="abs service-box" style="left:98px"><ul>
  <li>Training &amp; Development</li><li>Employee Handbooks</li><li>Labor Law Compliance</li><li>Job Descriptions</li><li>Help Center</li><li>Recruiting</li><li>Career Opportunities</li><li>Background Screening</li><li>KPEO WebSmart</li><li>E-Check</li>
</ul></div>
<div class="abs service-box" style="left:341px;width:227px;padding-left:23px"><ul>
  <li>Payroll Administration</li><li>Tax Payment and Filing</li><li>Online Payroll Entry</li><li>Paycard</li><li>Time &amp; Attendance</li><li>General Ledger Interface</li><li>ASO Services</li><li>KPower.</li>
</ul></div>
<div class="abs service-box" style="left:583px;width:228px;padding-left:25px"><ul>
  <li>Policy Administration</li><li>Injury Claim Administration</li><li>Safety Compliance &amp; Audits</li><li>Safety Compliance Services</li><li>Safety Training Classes</li>
</ul></div>

<svg class="abs slide-arrow" style="left:69px" width="22" height="22" viewBox="0 0 22 22"><circle cx="11" cy="11" r="10.5" fill="#bdbdbd"/><path d="M13 6 L8 11 L13 16" fill="none" stroke="#fff" stroke-width="2.2"/></svg>
<svg class="abs slide-arrow" style="left:817px" width="22" height="22" viewBox="0 0 22 22"><circle cx="11" cy="11" r="10.5" fill="#bdbdbd"/><path d="M9 6 L14 11 L9 16" fill="none" stroke="#fff" stroke-width="2.2"/></svg>

<footer class="abs footer"></footer>
<h4 class="abs f-head" style="left:98px">Quick Links</h4>
<h4 class="abs f-head" style="left:341px">Support Links</h4>
<h4 class="abs f-head" style="left:463px">Newsletter SignUp</h4>
<h4 class="abs f-head" style="left:705px">Connect With Us</h4>

<ul class="abs f-list" style="left:98px;top:1012px;line-height:19.4px">
  <li>Home</li><li>About Us</li><li>Request a Quote</li><li>Contact Us</li><li>Sitemap</li><li>Demo</li>
</ul>
<ul class="abs f-list" style="left:220px;top:1012px;line-height:22.4px">
  <li>Payroll Services</li><li>HR Solutions</li><li>Online Solutions</li><li>Workers Comp</li><li>&nbsp;Employee's Benefit's</li><li>Resources</li>
</ul>
<ul class="abs f-list" style="left:341px;top:1012px;line-height:18.4px">
  <li>Legal Notice</li><li>Privacy Policy</li><li>Terms &amp; Conditions</li><li>Help</li>
</ul>

<p class="abs news-text">Sign-up for our daily emails by entering your information below:</p>
<div class="abs field" style="top:1047px">Name</div>
<div class="abs field" style="top:1079px">Enter Your E-Mail ID</div>
<a class="abs subscribe">Subscribe</a>

<div class="abs social" style="top:1009px"><i></i><span>Updates</span></div>
<div class="abs social" style="top:1037px"><i></i><span>Community</span></div>
<div class="abs social" style="top:1066px"><i></i><span>Network</span></div>

<p class="abs copy">Copyright ©2013 Company Name &nbsp;&nbsp; - All rights reserved</p>

</body>
</html>
```